Tirovel

We need a business card for our company is a holding for different business all are different we try to have some air of relax and fun in our projects we add pictures of the office to give you an idea od the mood of the business

Business

```html
<!DOCTYPE html>
<html lang="en">
<head>
<meta charset="utf-8">
<title>Tirovel – Business Card</title>
<link href="https://fonts.googleapis.com/css2?family=Exo+2:wght@400;600;700&display=swap" rel="stylesheet">
<style>
  :root {
    --canvas: #e9e4da;
    --card: #fbfbfb;
    --card-edge: #e2e2e2;
    --yellow: #f6e51b;
    --yellow-deep: #eed400;
    --brown: #6f4a2c;
    --brown-light: #a07a58;
    --ink: #4a4a4a;
    --white: #ffffff;
  }
  * { margin: 0; padding: 0; box-sizing: border-box; }
  html, body {
    width: 1057px; height: 1200px; overflow: hidden;
    background: var(--canvas);
    font-family: "Exo 2", sans-serif;
  }
  .sheet {
    position: relative; width: 1057px; height: 1200px;
    display: flex; justify-content: center; align-items: center; gap: 77px;
  }
  .card {
    position: relative; width: 400px; height: 700px;
    background: linear-gradient(160deg, var(--white) 0%, var(--card) 60%, #f1f1f1 100%);
    border: 1px solid var(--card-edge);
    box-shadow: 0 14px 30px rgba(60, 45, 25, 0.18);
    overflow: hidden;
  }
  .brand {
    position: absolute; display: flex; align-items: center; gap: 10px;
    color: var(--brown); font-weight: 700; letter-spacing: 0.5px;
  }
  .brand-mark { background: var(--yellow); display: block; }
  .card--front .brand { top: 58px; right: 48px; font-size: 38px; }
  .card--front .brand-mark { width: 26px; height: 26px; }
  .card--back .brand { top: 250px; left: 50%; transform: translateX(-50%); font-size: 50px; }
  .card--back .brand-mark { width: 34px; height: 34px; }

  .contact {
    position: absolute; top: 150px; left: 120px;
    list-style: none; color: var(--ink); font-size: 14px; line-height: 1.3;
  }
  .contact li { display: flex; align-items: center; gap: 9px; margin-bottom: 12px; }
  .contact .address { display: block; margin-bottom: 18px; font-size: 15px; }
  .icon {
    width: 20px; height: 20px; background: var(--brown); border-radius: 3px;
    display: flex; align-items: center; justify-content: center; flex: none;
  }
  .icon svg { width: 12px; height: 12px; fill: none; stroke: var(--white); stroke-width: 2; stroke-linecap: round; stroke-linejoin: round; }

  .footer-band { position: absolute; left: 0; bottom: 0; width: 400px; height: 230px; display: block; }
  .holder {
    position: absolute; right: 34px; bottom: 34px; text-align: right;
    color: var(--white); text-transform: uppercase; letter-spacing: 2px;
    line-height: 1.2;
  }
  .holder-name { font-size: 24px; font-weight: 600; }
  .holder-role { font-size: 17px; font-weight: 400; margin-top: 6px; }
  .web-back {
    position: absolute; left: 90px; bottom: 40px; font-size: 13px;
    color: var(--brown-light); letter-spacing: 1px;
  }
</style>
</head>
<body>
<main class="sheet">

  <section class="card card--front" aria-label="Card front">
    <div class="brand"><span class="brand-mark"></span>Tirovel</div>

    <ul class="contact">
      <li class="address">42 Linden Park Road,<br>2nd building Street</li>
      <li><span class="icon"><svg viewBox="0 0 12 12"><path d="M3 1.5l1.5 2.5-1 1c.6 1.3 1.5 2.2 2.5 2.8l1-1L9.5 8 8.5 10C5 9.5 2.5 7 2 3.5z"/></svg></span>021 555 0147</li>
      <li><span class="icon"><svg viewBox="0 0 12 12"><rect x="3" y="1" width="6" height="10" rx="1"/><path d="M5.5 9h1"/></svg></span>021 555 0148</li>
      <li><span class="icon"><svg viewBox="0 0 12 12"><rect x="2" y="4" width="8" height="6"/><path d="M3.5 4V1.5h5V4"/></svg></span>021 555 0149</li>
      <li><span class="icon"><svg viewBox="0 0 12 12"><rect x="1.5" y="2.5" width="9" height="7"/><path d="M1.5 3l4.5 3.5L10.5 3"/></svg></span>hello@tirovel.com</li>
      <li><span class="icon"><svg viewBox="0 0 12 12"><circle cx="6" cy="6" r="4.5"/><path d="M1.5 6h9M6 1.5c2 2.5 2 6.5 0 9M6 1.5c-2 2.5-2 6.5 0 9"/></svg></span>www.tirovel.com</li>
    </ul>

    <svg class="footer-band" viewBox="0 0 400 230" aria-hidden="true">
      <path d="M0 50 C120 20 280 30 400 80 L400 230 L0 230 Z" fill="var(--yellow)"/>
      <path d="M0 68 C125 40 280 50 400 96 L400 230 L0 230 Z" fill="var(--white)"/>
      <path d="M0 78 C130 52 282 62 400 106 L400 230 L0 230 Z" fill="var(--yellow-deep)"/>
      <path d="M0 94 C135 68 285 78 400 120 L400 230 L0 230 Z" fill="var(--white)"/>
      <path d="M0 102 C140 78 290 88 400 128 L400 230 L0 230 Z" fill="var(--brown)"/>
    </svg>
    <div class="holder">
      <div class="holder-name">Marco Velden</div>
      <div class="holder-role">General Manager</div>
    </div>
  </section>

  <section class="card card--back" aria-label="Card back">
    <div class="brand"><span class="brand-mark"></span>Tirovel</div>
    <svg class="footer-band" viewBox="0 0 400 230" aria-hidden="true">
      <path d="M0 50 C120 20 280 30 400 80 L400 230 L0 230 Z" fill="var(--yellow)"/>
      <path d="M0 68 C125 40 280 50 400 96 L400 230 L0 230 Z" fill="var(--white)"/>
      <path d="M0 78 C130 52 282 62 400 106 L400 230 L0 230 Z" fill="var(--yellow-deep)"/>
      <path d="M0 94 C135 68 285 78 400 120 L400 230 L0 230 Z" fill="var(--white)"/>
      <path d="M0 102 C140 78 290 88 400 128 L400 230 L0 230 Z" fill="var(--brown)"/>
    </svg>
    <div class="web-back">www.tirovel.com</div>
  </section>

</main>
</body>
</html>
```